Fenwick & Associates Holdings Business Cards

Max 4/4 (4 Colors each side) Business Cards
Size 85 x 55 mm
Fenwick & Associates Holdings Ltd. (3 Versions of the Logo attached)
Possibility to add second company name as we have different subsidiary companies
Name, Position, E-Mail, Direct Phone, (optional Cell Phone)
Possibility to change the address as we have offices in London an Zurich
Font for Name, Address, etc.: Source Sans Pro Light (Google Fonts)
PDF and Source Files to send them directly to offset

Industry/Entity Type

Business

Font styles to use
Sans Serif
Script

```html
<!DOCTYPE html>
<html lang="en">
<head>
<meta charset="utf-8">
<title>Fenwick &amp; Associates Holdings – Business Cards</title>
<link rel="stylesheet" href="https://fonts.googleapis.com/css2?family=Source+Sans+3:wght@300;400;600&family=Tinos&display=swap">
<style>
  :root {
    --stage: #e6e6e6;
    --paper: #ffffff;
    --brand-blue: #1c5fa8;
    --ink-grey: #6b6b6b;
    --card-dark: #26292c;
    --card-dark-deep: #1b1d1f;
    --text-light: #e4e6e8;
    --icon-blue: #2f78c4;
  }
  * { box-sizing: border-box; margin: 0; padding: 0; }
  html, body { width: 1200px; height: 900px; overflow: hidden; }
  body {
    background: var(--stage);
    font-family: "Source Sans 3", Arial, sans-serif;
    position: relative;
  }
  .card {
    position: absolute;
    top: 288px;
    width: 500px;
    height: 324px;
    border-radius: 22px;
    overflow: hidden;
  }
  .card--front { left: 70px; background: var(--card-dark); }
  .card--back {
    left: 630px;
    background: radial-gradient(ellipse at 45% 40%, var(--card-dark) 0%, var(--card-dark-deep) 100%);
  }

  /* front */
  .front-header {
    position: absolute; inset: 0 0 auto 0;
    height: 150px;
    background: var(--paper);
  }
  .front-rule {
    position: absolute; left: 0; right: 0; top: 150px;
    height: 9px;
    background: var(--brand-blue);
  }
  .front-body {
    position: absolute; left: 0; right: 0; top: 159px; bottom: 0;
    background: linear-gradient(180deg, #2c2f32 0%, var(--card-dark-deep) 100%);
  }
  .holder {
    position: absolute; right: 34px; top: 22px;
    text-align: right;
  }
  .holder-name { font-size: 19px; font-weight: 400; color: var(--brand-blue); line-height: 1.1; }
  .holder-role { font-size: 13px; font-weight: 300; color: #444; margin-top: 2px; }

  .brand { display: flex; align-items: center; gap: 12px; }
  .brand-mark { background: var(--brand-blue); flex: none; }
  .brand-name {
    font-family: "Tinos", "Times New Roman", serif;
    color: var(--brand-blue);
    text-transform: uppercase;
    letter-spacing: 0.5px;
    white-space: nowrap;
  }
  .front-brand { position: absolute; left: 48px; top: 86px; }
  .front-brand .brand-mark { width: 26px; height: 26px; }
  .front-brand .brand-name { font-size: 20px; }

  .contact {
    position: absolute; left: 30px; top: 174px;
    color: var(--text-light);
    font-size: 13px; font-weight: 300; line-height: 17px;
    list-style: none;
  }
  .contact li { display: flex; gap: 6px; }
  .contact svg { width: 13px; height: 13px; flex: none; margin-top: 2px; fill: var(--icon-blue); }
  .contact .gap { margin-top: 8px; }

  /* back */
  .back-brand {
    position: absolute; left: 0; right: 0; top: 0; bottom: 0;
    justify-content: center;
  }
  .back-brand .brand-mark { width: 30px; height: 30px; }
  .back-brand .brand-name { font-size: 24px; color: #2a6bb5; }
</style>
</head>
<body>

<section class="card card--front" aria-label="Business card front">
  <div class="front-header"></div>
  <div class="front-rule"></div>
  <div class="front-body"></div>

  <div class="holder">
    <p class="holder-name">Lena Marsh</p>
    <p class="holder-role">Manager</p>
  </div>

  <div class="brand front-brand">
    <span class="brand-mark"></span>
    <span class="brand-name">Fenwick &amp; Associates Holdings</span>
  </div>

  <ul class="contact">
    <li>
      <svg viewBox="0 0 16 16"><path d="M8 1 1 7.5h2V15h4v-4h2v4h4V7.5h2z"/></svg>
      <span>Seefeldweg 48<br>8008 Zürich<br>Switzerland</span>
    </li>
    <li class="gap">
      <svg viewBox="0 0 16 16"><path d="M4 1h8v14H4zM5.5 3v9h5V3zM7 13h2v1H7z" fill-rule="evenodd"/></svg>
      <span>41 44 210 58 10</span>
    </li>
    <li>
      <svg viewBox="0 0 16 16"><path d="M3 1l3 3-2 2c1 2 4 5 6 6l2-2 3 3-2 2C7 15 1 9 1 3z"/></svg>
      <span>+41 44 210 58 11</span>
    </li>
    <li>
      <svg viewBox="0 0 16 16"><path d="M4 1h8v4H4zM1 6h14v6h-3v3H4v-3H1zM5 10v4h6v-4z" fill-rule="evenodd"/></svg>
      <span>+41 44 210 58 12</span>
    </li>
    <li class="gap">
      <svg viewBox="0 0 16 16"><path d="M1 3h14v1L8 9 1 4zM1 5.5l7 5 7-5V13H1z"/></svg>
      <span>lena@fenwickholdings.com</span>
    </li>
  </ul>
</section>

<section class="card card--back" aria-label="Business card back">
  <div class="brand back-brand">
    <span class="brand-mark"></span>
    <span class="brand-name">Fenwick &amp; Associates Holdings</span>
  </div>
</section>

</body>
</html>
```